English and Spanish Language School Needs a Business Card

Need a business card design a startup company called Corvelle Language School. The company will offer English and Spanish conversational level courses designed to make the learner feel comfortable with grammar and vocabulary. We would like to see a logo with some colour that should communicate learning, growth.

Target Market(s)

Consumers and businesses

Industry/Entity Type

Education

Contact Information for Business Card

TBD

Font styles to use
Serif

Requirements
Must have
• Include the following
• Logo
• Name
• Title
• Cellphone Number
• Office Phone number
• Email address
• Office Address

```html
<!DOCTYPE html>
<html lang="en">
<head>
<meta charset="utf-8">
<title>Corvelle Language School – Business Card</title>
<link href="https://fonts.googleapis.com/css2?family=Questrial&display=swap" rel="stylesheet">
<style>
  :root {
    --page: #e7e3de;
    --card: #f4f3f1;
    --red: #b3262e;
    --teal: #1f7f86;
    --ink: #3a3a3c;
  }
  html, body {
    margin: 0;
    width: 1200px;
    height: 969px;
    overflow: hidden;
    background: var(--page);
    font-family: "Questrial", "Century Gothic", sans-serif;
  }
  .card {
    position: absolute;
    left: 100px;
    top: 199px;
    width: 1000px;
    height: 571px;
    background: var(--card);
    border-radius: 30px;
    overflow: hidden;
    box-shadow: 0 10px 30px rgba(0,0,0,0.12);
  }
  .edge-tab {
    position: absolute;
    left: -22px;
    top: 193px;
    width: 44px;
    height: 44px;
    border-radius: 50%;
    background: var(--red);
  }
  .brand-mark {
    position: absolute;
    left: 588px;
    top: 82px;
    width: 410px;
    height: 410px;
    border-radius: 50%;
    background: var(--red);
  }
  .wordmark {
    position: absolute;
    left: 48px;
    top: 38px;
    color: var(--red);
    line-height: 1;
  }
  .wordmark .name {
    display: block;
    font-size: 88px;
    letter-spacing: -1px;
  }
  .wordmark .sub {
    display: block;
    font-size: 25px;
    margin-top: 4px;
    margin-left: 4px;
  }
  .person {
    position: absolute;
    left: 48px;
    top: 192px;
  }
  .person .full-name {
    margin: 0;
    font-size: 36px;
    font-weight: 400;
    color: var(--red);
    letter-spacing: 0.5px;
  }
  .person .role {
    margin: 6px 0 0;
    font-size: 29px;
    color: var(--teal);
    letter-spacing: 0.5px;
  }
  .address {
    position: absolute;
    left: 48px;
    top: 296px;
    font-style: normal;
    font-size: 27px;
    line-height: 37px;
    color: var(--ink);
  }
  .contacts {
    position: absolute;
    left: 48px;
    top: 384px;
    margin: 0;
    padding: 0;
    list-style: none;
    font-size: 27px;
    line-height: 38px;
    color: var(--ink);
  }
  .contacts li {
    display: flex;
    align-items: center;
  }
  .contacts svg {
    width: 24px;
    height: 24px;
    margin-right: 16px;
    fill: var(--red);
    flex: none;
  }
</style>
</head>
<body>
  <main class="card">
    <div class="edge-tab"></div>
    <div class="brand-mark" role="img" aria-label="Large brand mark area"></div>

    <div class="wordmark">
      <span class="name">Corvelle</span>
      <span class="sub">Language School</span>
    </div>

    <div class="person">
      <h1 class="full-name">MAREN HOLT</h1>
      <p class="role">CEO/FOUNDER</p>
    </div>

    <address class="address">
      412 Larkspur Court<br>
      Fairbanks, Alaska 99701
    </address>

    <ul class="contacts">
      <li>
        <svg viewBox="0 0 24 24" aria-hidden="true"><path d="M6.6 10.8a15.1 15.1 0 0 0 6.6 6.6l2.2-2.2a1 1 0 0 1 1-.25 11.4 11.4 0 0 0 3.6.57 1 1 0 0 1 1 1V20a1 1 0 0 1-1 1A17 17 0 0 1 3 4a1 1 0 0 1 1-1h3.5a1 1 0 0 1 1 1c0 1.25.2 2.45.57 3.57a1 1 0 0 1-.25 1z"/></svg>
        555 214 7730
      </li>
      <li>
        <svg viewBox="0 0 24 24" aria-hidden="true"><path d="M7 1h10a2 2 0 0 1 2 2v18a2 2 0 0 1-2 2H7a2 2 0 0 1-2-2V3a2 2 0 0 1 2-2zm0 3v14h10V4zm5 15.5a1.2 1.2 0 1 0 0 2.4 1.2 1.2 0 0 0 0-2.4z"/></svg>
        555 380 1946
      </li>
      <li>
        <svg viewBox="0 0 24 24" aria-hidden="true"><path d="M2 5h20v14H2zm2 2v.4l8 5 8-5V7zm0 2.8V17h16V9.8l-8 5z"/></svg>
        hello@corvelle.example
      </li>
      <li>
        <svg viewBox="0 0 24 24" aria-hidden="true"><path d="M12 2a10 10 0 1 0 0 20 10 10 0 0 0 0-20zm6.9 9h-3a15 15 0 0 0-1.3-6A8 8 0 0 1 18.9 11zM12 4.1c.9 1.3 1.7 3.8 1.9 6.9h-3.8c.2-3.1 1-5.6 1.9-6.9zM4.1 13h3a15 15 0 0 0 1.3 6A8 8 0 0 1 4.1 13zm3-2h-3a8 8 0 0 1 4.3-6 15 15 0 0 0-1.3 6zm4.9 8.9c-.9-1.3-1.7-3.8-1.9-6.9h3.8c-.2 3.1-1 5.6-1.9 6.9zm2.6-.9a15 15 0 0 0 1.3-6h3a8 8 0 0 1-4.3 6z"/></svg>
        www.corvelle.example
      </li>
    </ul>
  </main>
</body>
</html>
```